A reimagined website for a cross-border tax firm

There are two aspects to this project for Brindlemoor Tax Advisory:
1) I need a logo update to accommodate increasing focus and specialization in my business. The byline under the name “Brindlemoor Tax Advisory” needs to change:
ORIGINAL: TAX SUPPORT FOR PUBLIC ACCOUNTING FIRMS
REVISED: CROSS-BORDER TAX SERVICES • U.S. & CANADA
2) I need a website “refresh” (see current website at www.levyhelpdesk.example) based on this logo – a new vision for a website with greater clarity, focus and organization. It should represent a re-envisioning of the current approach, and not the wholesale abandonment of the style represented there. I need it to be creative, compelling and attention grabbing, but still professional. This should, at a minimum, update any places where the old name/logo is used, but I want the redesign to go beyond this to something more intuitive. I need high quality separate PNG files of the various logo styles for use in various documents, but HTML coding would be a helpful but not necessary addition.

Target Market(s)

People in need of cross-border tax services - Canada and US

Coding

Number of Pages Required

Requirements
Must have
• Greater crispness, sharpness - higher resolution
• A more compelling, organized approach - make the wording and images more accessible to the website user (especially the staff bios, which have scroll bars now)
Nice to have
• Replacement of stock image with a true image of the Halifax skyline
Should not have
• Deviate from colour pattern represented in website logo of blue/orange
• Deviate from existing logo except for word replacement

```html
<!DOCTYPE html>
<html lang="en">
<head>
<meta charset="utf-8">
<title>Brindlemoor Tax Advisory</title>
<link href="https://fonts.googleapis.com/css2?family=Roboto:wght@300;400;500;700&display=swap" rel="stylesheet">
<style>
:root{
  --orange:#f26a25;
  --orange-light:#f58243;
  --orange-dark:#ea6020;
  --navy:#1d3f6e;
  --ink:#3a3a3a;
  --text:#555;
  --muted:#8a8a8a;
  --line:#e3e3e3;
  --footer-bg:#ececec;
  --bar-bg:#4b4b4b;
  --white:#fff;
}
*{box-sizing:border-box;margin:0;padding:0}
html,body{width:1200px;height:2782px;overflow:hidden;background:var(--white)}
body{position:relative;font-family:'Roboto',Arial,sans-serif;color:var(--text)}
.abs{position:absolute}

/* hero */
.hero{left:0;top:0;width:1200px;height:618px;
  background:
    radial-gradient(ellipse 260px 330px at 585px 330px,rgba(120,104,92,.85),rgba(120,104,92,0) 70%),
    radial-gradient(ellipse 220px 200px at 1000px 400px,rgba(150,86,48,.75),rgba(150,86,48,0) 70%),
    radial-gradient(ellipse 260px 160px at 250px 420px,rgba(96,80,70,.8),rgba(96,80,70,0) 70%),
    linear-gradient(180deg,#5c5b66 0%,#7b7880 22%,#8d8384 38%,#7a6456 55%,#5e4838 68%,#3d3530 76%,#4b4f58 82%,#3a414b 100%)}
.topbar{left:161px;top:6px;height:24px;display:flex;align-items:center;gap:22px;font-size:12px;letter-spacing:1.5px;color:var(--white);white-space:nowrap}
.topbar .item{display:flex;align-items:center;gap:8px}
.dot{width:20px;height:20px;border-radius:50%;background:var(--orange);display:flex;align-items:center;justify-content:center}
.social{right:161px;top:7px;display:flex;gap:8px}
.social span{width:22px;height:22px;border-radius:50%;background:var(--orange);display:block}
.nav{left:161px;top:37px;width:878px;height:67px;background:var(--white);display:flex;align-items:center;padding:0 14px 0 10px;white-space:nowrap}
.brand{display:flex;align-items:center;gap:7px}
.brand .sq{width:22px;height:22px;background:var(--navy)}
.brand .name{font-size:15px;font-weight:700;color:var(--navy);letter-spacing:.3px;line-height:1}
.brand .byline{font-size:7px;color:var(--navy);letter-spacing:.5px;margin-top:4px;border-top:1px solid var(--navy);padding-top:2px}
.menu{margin-left:auto;display:flex;gap:27px;font-size:10.5px;letter-spacing:.6px;color:var(--ink);height:100%;align-items:center}
.menu .active{color:var(--orange);position:relative}
.menu .active:after{content:"";position:absolute;left:-4px;right:-4px;bottom:-18px;height:2px;background:var(--orange)}
.hero-title{left:0;width:1200px;top:257px;text-align:center;color:var(--white);white-space:nowrap}
.hero-title .l1{font-weight:300;font-size:45px;letter-spacing:3px;line-height:52px}
.hero-title .l2{font-weight:700;font-size:46px;letter-spacing:1px;line-height:48px}
.slide-btn{top:273px;width:22px;height:80px;border:1px solid rgba(255,255,255,.6);color:var(--white);font-size:11px;letter-spacing:3px;writing-mode:vertical-rl;display:flex;align-items:center;justify-content:center}

/* services */
.services{left:161px;top:514px;width:878px;height:189px;display:flex}
.svc{flex:1;display:flex;align-items:flex-start;padding:22px 20px 0 28px;gap:28px;color:var(--white)}
.svc.ind{background:var(--orange-light)}
.svc.paf{background:var(--orange-dark)}
.svc h3{font-weight:400;font-size:16px;letter-spacing:.8px;margin-bottom:10px;white-space:nowrap}
.svc p{font-size:10.5px;line-height:15px}
.svc .btn{display:inline-block;margin-top:12px;border:1px solid var(--white);font-size:9.5px;padding:5px 8px;letter-spacing:.5px}

/* section headings */
.kicker{left:0;width:1200px;text-align:center;font-size:11px;letter-spacing:2px;color:var(--muted)}
.heading{left:0;width:1200px;text-align:center;font-size:23px;font-weight:500;letter-spacing:1px;color:var(--ink)}
.rule{left:545px;width:110px;height:1px;background:var(--line)}
.rule:after{content:"";position:absolute;left:37px;top:-1px;width:36px;height:3px;background:var(--orange)}

/* who we are */
.about-photo{left:161px;top:848px;width:429px;height:289px;
  background:
    radial-gradient(ellipse 90px 120px at 100px 200px,rgba(40,44,56,.9),rgba(40,44,56,0) 75%),
    radial-gradient(ellipse 80px 110px at 370px 200px,rgba(34,40,60,.9),rgba(34,40,60,0) 75%),
    radial-gradient(ellipse 90px 80px at 250px 190px,rgba(250,250,252,.95),rgba(250,250,252,0) 75%),
    linear-gradient(180deg,#dfe5ea 0%,#eef1f3 45%,#d7dde2 70%,#f3f4f5 100%)}
.about-text{left:618px;top:858px;width:421px}
.about-text h4{font-weight:400;font-size:17px;color:var(--ink);letter-spacing:.5px;margin-bottom:18px}
.about-text p{font-size:11px;line-height:21px;letter-spacing:.3px;margin-bottom:18px}

/* team */
.photo{background:
  radial-gradient(ellipse 70px 150px at 50% 62%,rgba(30,30,34,.85),rgba(30,30,34,0) 80%),
  radial-gradient(ellipse 140px 180px at 50% 40%,#6a6a6a,#3a3a3a 90%)}
.photo.light{background:
  radial-gradient(ellipse 70px 150px at 50% 62%,rgba(236,236,236,.9),rgba(236,236,236,0) 80%),
  radial-gradient(ellipse 140px 180px at 50% 40%,#767676,#484848 90%)}
.photo .frame{position:absolute;left:16px;top:16px;right:16px;bottom:16px;border:1px solid rgba(255,255,255,.7)}
.bio{background:var(--white);box-shadow:0 0 6px rgba(0,0,0,.12);padding:16px 18px}
.bio h4{font-weight:500;font-size:13px;letter-spacing:.8px;color:var(--ink);margin-bottom:6px}
.bio p{font-size:9.6px;line-height:19.6px;color:var(--text)}

/* contact */
.contact-band{left:0;top:2319px;width:1200px;height:393px;background:var(--footer-bg)}
.contact-card{left:161px;top:2378px;width:353px;height:278px;background:var(--white);padding:14px 12px}
.contact-card h5,.form-title{font-size:12.5px;font-weight:700;letter-spacing:.5px;color:var(--ink)}
.crow{display:flex;align-items:center;gap:16px;border-top:1px solid var(--line);height:54px;font-size:10px;line-height:17px;color:var(--ink)}
.crow:first-of-type{margin-top:12px}
.crow .dot{width:28px;height:28px;flex:none;margin-left:4px}
.form-title{left:536px;top:2391px}
.field{background:var(--white);font-size:9.5px;color:var(--ink);letter-spacing:.5px;padding:9px 7px}
.submit{left:536px;top:2619px;width:91px;height:37px;background:var(--orange);color:var(--white);font-size:10px;font-weight:500;display:flex;align-items:center;justify-content:center;letter-spacing:.5px}
.bottom-bar{left:0;top:2712px;width:1200px;height:70px;background:var(--bar-bg);color:#ddd;font-size:9px;font-weight:500;letter-spacing:.4px}
.bottom-bar .left{left:161px;top:30px}
.bottom-bar .right{right:161px;top:30px}
</style>
</head>
<body>

<div class="abs hero" role="img" aria-label="City skyline photograph with tall office towers above a waterfront at dusk"></div>

<div class="abs topbar">
  <div class="item"><span class="dot"><svg width="10" height="10" viewBox="0 0 10 10"><path d="M2 1l2 2-1 1c.6 1.3 1.6 2.3 3 3l1-1 2 2-1.5 1.5C4.5 9 1 5.5 .5 2.5z" fill="#fff"/></svg></span>(555) 014-2290</div>
  <div class="item"><span class="dot"><svg width="10" height="10" viewBox="0 0 10 10"><path d="M2 1l2 2-1 1c.6 1.3 1.6 2.3 3 3l1-1 2 2-1.5 1.5C4.5 9 1 5.5 .5 2.5z" fill="#fff"/></svg></span>(555) 014-2290</div>
</div>
<div class="abs social"><span></span><span></span><span></span></div>

<nav class="abs nav">
  <div class="brand">
    <span class="sq"></span>
    <div>
      <div class="name">BRINDLEMOOR TAX ADVISORY</div>
      <div class="byline">CROSS-BORDER TAX SERVICES • U.S. &amp; CANADA</div>
    </div>
  </div>
  <div class="menu">
    <span class="active">HOME</span><span>OUR TEAM</span><span>INDIVIDUALS</span><span>PUBLIC ACCOUNTING FIRMS</span><span>CONTACT</span><span>PAYMENT</span>
  </div>
</nav>

<div class="abs slide-btn" style="left:15px">PREV</div>
<div class="abs slide-btn" style="right:15px">NEXT</div>

<div class="abs hero-title">
  <div class="l1">CROSS-BORDER TAX SERVICES</div>
  <div class="l2">U.S. &amp; CANADA</div>
</div>

<section class="abs services">
  <div class="svc ind">
    <svg width="120" height="110" viewBox="0 0 120 110" style="flex:none;margin-top:20px">
      <circle cx="60" cy="55" r="50" fill="none" stroke="#fff" stroke-width="7"/>
      <circle cx="60" cy="42" r="17" fill="none" stroke="#fff" stroke-width="7"/>
      <path d="M28 90c6-16 18-24 32-24s26 8 32 24" fill="none" stroke="#fff" stroke-width="7"/>
    </svg>
    <div>
      <h3>FOR INDIVIDUALS</h3>
      <p>We are firm devoted to helping individuals and businesses determine, comply with and minimize/optimize their Canadian and U.S. tax obligations. Let's take a moment to unpack that sentence.</p>
      <span class="btn">LEARN MORE ❯</span>
    </div>
  </div>
  <div class="svc paf">
    <svg width="110" height="110" viewBox="0 0 110 110" style="flex:none;margin-top:18px">
      <rect x="30" y="6" width="42" height="96" fill="none" stroke="#fff" stroke-width="6"/>
      <rect x="6" y="48" width="24" height="54" fill="none" stroke="#fff" stroke-width="6"/>
      <rect x="72" y="38" width="32" height="64" fill="none" stroke="#fff" stroke-width="6"/>
      <g fill="#fff"><rect x="40" y="18" width="8" height="8"/><rect x="54" y="18" width="8" height="8"/><rect x="40" y="34" width="8" height="8"/><rect x="54" y="34" width="8" height="8"/><rect x="40" y="50" width="8" height="8"/><rect x="54" y="50" width="8" height="8"/><rect x="14" y="62" width="8" height="8"/><rect x="14" y="78" width="8" height="8"/><rect x="82" y="52" width="12" height="8"/><rect x="82" y="70" width="12" height="8"/><rect x="46" y="80" width="10" height="22"/></g>
    </svg>
    <div>
      <h3>PUBLIC ACCOUNTING FIRMS</h3>
      <p>We provide a range of services to Canadian public accounting firms (PAF's) to assist them in serving their clients In general, our PAF clients are small firms which are not large enough.</p>
      <span class="btn">LEARN MORE ❯</span>
    </div>
  </div>
</section>

<div class="abs kicker" style="top:748px">LOREM IPSUM DOLOR SIT AMET</div>
<h2 class="abs heading" style="top:768px">WHO WE ARE</h2>
<div class="abs rule" style="top:809px"></div>

<div class="abs about-photo" role="img" aria-label="Photograph of three colleagues meeting at a table in a bright office"></div>
<div class="abs about-text">
  <h4>Suspendisse at ligula sodales</h4>
  <p>Lorem ipsum dolor sit amet, consectetur adipiscing elit. Sed dignissim justo vel nibh sagittis, eu lobortis risus tempor. Nunc ultrices risus a luctus accumsan. Vivamus vitae justo auctor, convallis quam sed, tempus est. Aliquam et tortor faucibus, congue turpis sit amet, luctus est. Aenean fermentum metus et felis commodo malesuada at at diam. Sed convallis dignissim massa, quis auctor sem ultrices ut. Ut odio ex, tempor vitae gravida eget, posuere sed sem.</p>
  <p>Lorem ipsum dolor sit amet, consectetur adipiscing elit. Sed dignissim justo vel nibh sagittis, eu lobortis risus tempor. Nunc ultrices risus a luctus accumsan. Vivamus vitae justo auctor, convallis quam sed, tempus</p>
</div>

<div class="abs kicker" style="top:1184px">LOREM IPSUM DOLOR SIT AMET</div>
<h2 class="abs heading" style="top:1204px">OUR TEAM</h2>
<div class="abs rule" style="top:1245px"></div>

<div class="abs photo" style="left:161px;top:1256px;width:225px;height:334px" role="img" aria-label="Portrait photograph of Martin R. Colwell"><div class="frame"></div></div>
<article class="abs bio" style="left:386px;top:1273px;width:653px;height:298px">
  <h4>MARTIN R. COLWELL, CPA, CGA, EA</h4>
  <p>Martin has been practicing tax for over 17 years.<br>
  Educated at Lakeshore University and Northfield College, he began his career in the Millbrook office of Hartwell &amp; Greer LLP in September 1998. After a short period in the audit practice, he transferred to the tax division where he focused on Canadian corporate and US personal tax compliance (that is, the preparation and filing of tax returns).<br>
  In January 2001 he took a position in the Ferncliff, Nova Scotia office of Ashdown Miller LLP, where he continued his work in US tax compliance. The other major component of his practice at this time was Canadian tax planning for owner-managed businesses. These emphases continued in his work for Pell &amp; Rowan Chartered Accountants in Glenport, Nova Scotia between January 2010 and June 2014. As a tax specialist in these multi-partner firms, he developed a passion for supporting general practitioners in the work of serving their clients.<br>
  In July 2014 Martin opened Brindlemoor Tax Advisory Inc. in Harborview, Nova Scotia - a business devoted to providing public accounting firms with tax support services.<br>
  Martin is chartered professional accountant (CPA) and an enrolled agent (EA). Enrolled agent status grants an individual unlimited practice rights before the IRS and is earned by passing a three-part exam administered by the IRS.</p>
</article>

<article class="abs bio" style="left:161px;top:1610px;width:653px;height:312px">
  <h4>OWEN PETRAKIS, CPA, CA</h4>
  <p>Owen has been practicing tax for over 7 years.<br>
  Educated at Bayside University in Harborview, where he graduated summa cum laude in 2005, Owen began his career at Calder Voss. After spending four years in the Audit and Assurance group, Owen transitioned to their tax department in 2008, where he gained experience in Canadian and U.S. compliance and Canadian and cross-border tax planning.<br>
  In 2012 Owen returned to his roots in the South Shore of Nova Scotia, joining the tax department of Tamsin Hale Partners in Riverton. His focus at Tamsin Hale was U.S. tax compliance, business valuation and tax planning engagements for owner-managers and their businesses.<br>
  Owen joined Brindlemoor Tax Advisory in July 2016 as a Senior Manager. Overseeing our Riverton office, he continues to provide a range of Canadian and U.S. compliance and advisory services to clients on the South Shore and beyond.<br>
  Owen received his chartered accountant designation in 2007 and has completed the first two parts of the CPAI In-Depth Tax Course.<br>
  Owen lives in Stillwater Cove with his wife and two children. He stays active in the community as the Treasurer for the Upper Brookvale Cemetery and as a member of the Cedar Point Residents Association.</p>
</article>
<div class="abs photo" style="left:814px;top:1592px;width:225px;height:337px" role="img" aria-label="Portrait photograph of Owen Petrakis"><div class="frame"></div></div>

<div class="abs photo light" style="left:161px;top:1929px;width:225px;height:336px" role="img" aria-label="Portrait photograph of Nora E. Colwell"><div class="frame"></div></div>
<article class="abs bio" style="left:386px;top:1948px;width:653px;height:300px">
  <h4>NORA E. COLWELL</h4>
  <p>Nora splits her time between Brindlemoor Tax Advisory and her part-time studies at Valley Ridge University, where she is pursuing a Bachelor of Business Administration degree.<br>
  When she is not working and studying, Nora enjoys reading and taking care of her two horses.</p>
</article>

<div class="abs contact-band"></div>
<div class="abs contact-card">
  <h5>CONTACT INFORMATION</h5>
  <div class="crow"><span class="dot"><svg width="12" height="14" viewBox="0 0 12 14"><path d="M6 0a5 5 0 0 1 5 5c0 4-5 9-5 9S1 9 1 5a5 5 0 0 1 5-5z" fill="#fff"/><circle cx="6" cy="5" r="2" fill="#f26a25"/></svg></span><span>418 KESTREL AVENUE, UNIT 12<br>HARBORVIEW, NOVA SCOTIA A1A 0A1</span></div>
  <div class="crow"><span class="dot"><svg width="12" height="14" viewBox="0 0 12 14"><path d="M6 0a5 5 0 0 1 5 5c0 4-5 9-5 9S1 9 1 5a5 5 0 0 1 5-5z" fill="#fff"/><circle cx="6" cy="5" r="2" fill="#f26a25"/></svg></span><span>55 MILLBROOK ROAD, UNIT 3<br>RIVERTON, NOVA SCOTIA A2B 0B2</span></div>
  <div class="crow"><span class="dot"><svg width="12" height="12" viewBox="0 0 10 10"><path d="M2 1l2 2-1 1c.6 1.3 1.6 2.3 3 3l1-1 2 2-1.5 1.5C4.5 9 1 5.5 .5 2.5z" fill="#fff"/></svg></span><span>(555) 014-2290</span></div>
  <div class="crow"><span class="dot"><svg width="12" height="12" viewBox="0 0 12 12"><rect x="2" y="1" width="8" height="10" fill="#fff"/><rect x="4" y="3" width="4" height="2" fill="#f26a25"/><rect x="4" y="7" width="4" height="2" fill="#f26a25"/></svg></span><span>(555) 014-2290</span></div>
</div>

<div class="abs form-title">SEND US A MESSAGE</div>
<div class="abs field" style="left:536px;top:2443px;width:239px;height:34px">NAME</div>
<div class="abs field" style="left:536px;top:2497px;width:239px;height:34px">PHONE</div>
<div class="abs field" style="left:536px;top:2551px;width:239px;height:34px">EMAIL</div>
<div class="abs field" style="left:800px;top:2443px;width:239px;height:141px">MESSAGE</div>
<div class="abs submit">SUBMIT</div>

<footer class="abs bottom-bar">
  <div class="abs left">COPYRIGHT © 2017 BRINDLEMOOR TAX ADVISORY INC.</div>
  <div class="abs right">TERMS OF USE AND PRIVACY POLICY</div>
</footer>

</body>
</html>
```